Meadowlark Learning Support Partners (MLSP)

This is a professional business card. Logo and picture are a must on the front of the card. I am an educational consultant. I have been consulting for the past three years for a company. I am now opening my own company. My goal for my consulting company is to eventually consult all over America.

Target Market(s)

Educators, schools, professionals

Industry/Entity Type

Consulting

Contact Information for Business Card

Picture/logo on front, simple modern design

Font styles to use
Serif

Colors
85abd2
0355a3
3176b5
cedeed

Requirements
Must have
• picture, logo,
• Dorotea Halvorsen, Ed.S
• address 5327 Quarry ridge Ln. Nashville, TN 37058
• Cell:616-555-0182
• Office: 629-555-0147
• www.Mlspwx.com
• halvorsendorotea@mailvexo.com

```html
<!DOCTYPE html>
<html lang="en">
<head>
<meta charset="utf-8">
<title>Meadowlark Learning Support Partners – Business Card</title>
<link rel="stylesheet" href="https://fonts.googleapis.com/css2?family=Jost:wght@400;500;700&display=swap">
<style>
  :root {
    --navy: #0355a3;
    --mid-blue: #3176b5;
    --soft-blue: #85abd2;
    --pale: #cedeed;
    --white: #ffffff;
    --backdrop: #e7ebf0;
  }
  * { box-sizing: border-box; margin: 0; padding: 0; }
  html, body { width: 1200px; height: 900px; overflow: hidden; }
  body {
    background: var(--backdrop);
    font-family: "Jost", sans-serif;
    display: flex;
    flex-direction: column;
    align-items: center;
    justify-content: center;
    gap: 48px;
  }
  .card {
    position: relative;
    width: 640px;
    height: 366px;
    overflow: hidden;
    box-shadow: 0 10px 28px rgba(3, 40, 80, 0.22);
  }

  /* Front */
  .card--front { background: var(--navy); }
  .card--front .band-mid {
    position: absolute; left: 0; right: 0; top: 230px; height: 18px;
    background: var(--mid-blue);
  }
  .card--front .band-light {
    position: absolute; left: 0; right: 0; top: 248px; height: 82px;
    background: linear-gradient(180deg, #dce8f3 0%, var(--pale) 100%);
  }
  .card--front .band-foot {
    position: absolute; left: 0; right: 0; top: 330px; bottom: 0;
    background: var(--mid-blue);
  }
  .brand {
    position: absolute;
    display: flex;
    align-items: center;
    color: var(--white);
  }
  .card--front .brand { left: 118px; top: 62px; }
  .brand__dot {
    width: 46px; height: 46px; border-radius: 50%;
    background: var(--white);
    margin-right: 16px;
  }
  .brand__short {
    font-weight: 700;
    font-size: 40px;
    letter-spacing: 3px;
  }
  .brand__rule {
    width: 1.5px; background: var(--white);
    align-self: stretch;
    margin: 0 18px;
  }
  .brand__full {
    font-weight: 500;
    font-size: 19px;
    line-height: 1.12;
  }

  /* Back */
  .card--back { background: var(--mid-blue); }
  .card--back .band-top {
    position: absolute; left: 0; right: 0; top: 0; height: 112px;
    background: var(--navy);
  }
  .card--back .band-name {
    position: absolute; left: 0; right: 0; top: 112px; height: 62px;
    background: linear-gradient(180deg, #dce8f3 0%, var(--pale) 100%);
    display: flex; align-items: center;
    padding-left: 60px;
  }
  .card--back .brand { left: 150px; top: 26px; }
  .card--back .brand__dot { width: 36px; height: 36px; margin-right: 12px; }
  .card--back .brand__short { font-size: 30px; letter-spacing: 2px; }
  .card--back .brand__rule { margin: 0 12px; }
  .card--back .brand__full { font-size: 13px; }
  .person-name {
    color: var(--navy);
    font-weight: 500;
    font-size: 34px;
    letter-spacing: 0.3px;
  }
  .contact {
    position: absolute; left: 0; right: 0; top: 190px;
    text-align: center;
    color: var(--white);
    font-size: 21px;
    line-height: 1.3;
  }
  .contact__address { font-size: 22px; margin-bottom: 2px; }
  .contact__gap { height: 12px; }
</style>
</head>
<body>

  <section class="card card--front" aria-label="Business card front">
    <div class="band-mid"></div>
    <div class="band-light"></div>
    <div class="band-foot"></div>
    <div class="brand">
      <span class="brand__dot"></span>
      <span class="brand__short">MLSP</span>
      <span class="brand__rule"></span>
      <span class="brand__full">Meadowlark<br>Learning<br>Support<br>Partners</span>
    </div>
  </section>

  <section class="card card--back" aria-label="Business card back">
    <div class="band-top"></div>
    <div class="brand">
      <span class="brand__dot"></span>
      <span class="brand__short">MLSP</span>
      <span class="brand__rule"></span>
      <span class="brand__full">Meadowlark<br>Learning<br>Support<br>Partners</span>
    </div>
    <div class="band-name">
      <h1 class="person-name">Dorotea Halvorsen, Ed.S</h1>
    </div>
    <address class="contact" style="font-style: normal;">
      <div class="contact__address">5327 Quarry ridge Ln. Nashville, TN 37058</div>
      <div>616-555-0182</div>
      <div>629-555-0147</div>
      <div class="contact__gap"></div>
      <div>www.Mlspwx.com</div>
      <div>halvorsendorotea@mailvexo.com</div>
    </address>
  </section>

</body>
</html>
```